8" x 11" One Page Flyer for Fence Installation Company

We are looking to promote our business with a new flyer that would be handed out in person to people or put at their mailbox/door at their homes. The flyer needs to be creative and attention-grabbing. I have attached some of our previous flyers and our website information. Do not call or email regarding the flyer. We want the flyer to look professional but also friendly. One page, NOT folded. You can use images from our website at www.MyBraxtonYard.com or our Facebook page at www.Facebook.com/HollowbrookRailsBKT. We are flexible with what photos you can use but there must be photos of OUR fences on the flyer. More photos specifically can also be provided. Colors need to be suitable for a flyer printed on canary yellow in color paper OR white paper.

Target Market(s)

Homeowners that need a new fence

Industry/Entity Type

Construction

Font styles to use
Sans Serif
Other font styles liked:
• HD Colton

Colors
0054AA
0677BA
7BADD7
CADEEF
E8F1F8
0094D4
00A9DD
6FCCEA
C7EBF8
E9F6FB

Requirements
Must have
• Our fence photos - mostly wood fence photos (different designs), SIZE SHOULD BE LETTER SIZE 8" x 11"
Nice to have
• A nice bible verse featured at the bottom of the flyer.
Should not have
• DO NOT COPY THE WEBSITE FORMAT, I WANT SOMETHING UNIQUE. Other people's fence photos, they must all come from our website or facebook page

```html
<!DOCTYPE html>
<html lang="en">
<head>
<meta charset="utf-8">
<title>Hollowbrook Rails Flyer</title>
<link href="https://fonts.googleapis.com/css2?family=Poppins:ital,wght@0,400;0,500;0,600;0,700;0,800;1,400;1,700;1,800&display=swap" rel="stylesheet">
<style>
  :root{
    --page-bg:#f2f2f2;
    --paper:#ffffff;
    --brand-blue:#3b7fc8;
    --deep-blue:#1d62ad;
    --panel-blue:#3d86c9;
    --ink:#1b1b1b;
    --brown:#5a3a26;
    --sun:#e8902e;
    --sky-top:#ffffff;
    --sky-mid:#cfe3f6;
    --tree:#5f8d3a;
    --grass:#6fa63a;
  }
  *{box-sizing:border-box;margin:0;padding:0}
  html,body{width:766px;height:1200px;overflow:hidden}
  body{background:var(--page-bg);font-family:'Poppins',sans-serif;position:relative}
  .flyer{position:absolute;left:13px;top:121px;width:740px;height:958px;background:var(--paper);overflow:hidden;box-shadow:0 4px 14px rgba(0,0,0,.12)}
  .hero-photo{position:absolute;left:0;top:140px;width:740px;height:565px;
    background:linear-gradient(180deg,var(--sky-top) 0%,var(--sky-mid) 22%,#b8c9b4 34%,var(--tree) 48%,var(--grass) 62%,#7cae45 100%)}
  .hero-house{position:absolute;right:0;top:150px;width:385px;height:330px;
    background:linear-gradient(180deg,#9aa4ad 0%,#b8c6d2 35%,#a9b8c4 100%);opacity:.85}
  .headline{position:absolute;left:36px;top:30px;color:var(--brand-blue);font-weight:800;font-size:54px;line-height:51px;letter-spacing:-.5px}
  .subline{position:absolute;left:38px;top:148px;font-style:italic;font-weight:700;font-size:19px;line-height:23px;color:var(--ink)}
  .brand{position:absolute;left:370px;top:28px;display:flex;align-items:flex-start;gap:12px}
  .brand-mark{width:62px;height:62px;background:var(--brown);margin-top:6px}
  .brand-text{display:flex;flex-direction:column}
  .brand-name{color:var(--brand-blue);font-weight:700;font-size:27px;line-height:32px}
  .brand-phone{color:var(--ink);font-weight:700;font-size:26px;line-height:32px}
  .brand-tag{color:var(--ink);font-weight:600;font-size:10px;line-height:16px}
  .cta-band{position:absolute;left:0;top:590px;width:740px;height:115px;background:var(--deep-blue)}
  .why-panel{position:absolute;left:35px;top:440px;width:295px;height:265px;background:var(--panel-blue);padding:12px 18px;color:#fff}
  .why-title{font-weight:800;font-size:24px;line-height:30px;margin-bottom:8px}
  .why-list{list-style:none}
  .why-list li{display:flex;align-items:center;gap:5px;font-size:14px;line-height:23px}
  .why-list b{font-weight:700}
  .tick{width:11px;height:11px;flex:none}
  .fine{font-size:7px;line-height:12px;padding-left:15px;opacity:.9}
  .cta{position:absolute;left:358px;top:603px;color:#fff}
  .cta-title{font-weight:800;font-size:25px;line-height:28px;letter-spacing:.5px}
  .cta-phone{font-weight:800;font-size:47px;line-height:50px;letter-spacing:1px}
  .cta-links{font-weight:600;font-size:12px;line-height:16px}
  .styles-title{position:absolute;left:0;top:720px;width:740px;text-align:center;color:var(--deep-blue);font-weight:700;font-size:22px;letter-spacing:4px}
  .styles{position:absolute;left:34px;top:758px;display:flex;gap:5px}
  .style-card{position:relative;width:165px;height:107px;border-radius:6px;overflow:hidden}
  .style-label{position:absolute;left:0;bottom:0;width:100%;height:19px;background:rgba(29,98,173,.9);color:#fff;font-weight:700;font-size:11px;line-height:19px;padding-left:8px}
  .picket{background:linear-gradient(180deg,#c9d7e3 0%,#e6c98a 30%,#d8b468 100%)}
  .privacy{background:linear-gradient(180deg,#b7c9d8 0%,#b08a5c 30%,#8c6a45 100%)}
  .split{background:linear-gradient(180deg,#c9d7e3 0%,#e9e2b8 40%,#9fb27a 100%)}
  .aluminum{background:linear-gradient(180deg,#d2dde6 0%,#6b7f63 45%,#4f6a3a 100%)}
  .footer{position:absolute;left:34px;top:893px;width:672px;display:flex;gap:14px;font-size:10px;line-height:12.5px;color:var(--ink)}
  .verse{width:280px;font-style:italic;padding-right:8px}
  .verse b{color:var(--deep-blue);font-weight:700;font-style:normal}
  .divider{width:1.5px;background:var(--deep-blue)}
  .hours b{font-weight:700}
  .hours .lead{color:var(--deep-blue)}
</style>
</head>
<body>
  <div class="flyer">
    <div class="hero-photo" role="img" aria-label="Photo of a split rail wood fence with wire mesh in a green lawn beside a grey sided house"></div>
    <div class="hero-house" role="img" aria-label="Grey sided house behind the fence"></div>

    <h1 class="headline">WE BUILD<br>FENCES....</h1>
    <p class="subline">And we would love to build<br>your fence too!</p>

    <div class="brand">
      <div class="brand-mark"></div>
      <div class="brand-text">
        <span class="brand-name">Hollowbrook Rails</span>
        <span class="brand-phone">555-014-2273</span>
        <span class="brand-tag">"Because Good Fences Make Good Neighbors"</span>
      </div>
    </div>

    <div class="cta-band"></div>

    <section class="why-panel">
      <h2 class="why-title">WHY CHOOSE US?</h2>
      <ul class="why-list">
        <li><svg class="tick" viewBox="0 0 12 12"><circle cx="6" cy="6" r="6" fill="#fff"/><path d="M3.2 6.2l1.9 1.9 3.7-3.9" stroke="#3d86c9" stroke-width="1.6" fill="none"/></svg><span><b>Free</b> Estimates</span></li>
        <li><svg class="tick" viewBox="0 0 12 12"><circle cx="6" cy="6" r="6" fill="#fff"/><path d="M3.2 6.2l1.9 1.9 3.7-3.9" stroke="#3d86c9" stroke-width="1.6" fill="none"/></svg><span>Professional Installation</span></li>
        <li><svg class="tick" viewBox="0 0 12 12"><circle cx="6" cy="6" r="6" fill="#fff"/><path d="M3.2 6.2l1.9 1.9 3.7-3.9" stroke="#3d86c9" stroke-width="1.6" fill="none"/></svg><span>Concrete in <b>EVERY</b> Post</span></li>
        <li><svg class="tick" viewBox="0 0 12 12"><circle cx="6" cy="6" r="6" fill="#fff"/><path d="M3.2 6.2l1.9 1.9 3.7-3.9" stroke="#3d86c9" stroke-width="1.6" fill="none"/></svg><span>HOA Submission Assistance</span></li>
        <li><svg class="tick" viewBox="0 0 12 12"><circle cx="6" cy="6" r="6" fill="#fff"/><path d="M3.2 6.2l1.9 1.9 3.7-3.9" stroke="#3d86c9" stroke-width="1.6" fill="none"/></svg><span>Lifetime Workmanship Warranty</span></li>
        <li><svg class="tick" viewBox="0 0 12 12"><circle cx="6" cy="6" r="6" fill="#fff"/><path d="M3.2 6.2l1.9 1.9 3.7-3.9" stroke="#3d86c9" stroke-width="1.6" fill="none"/></svg><span>Experienced Installation Teams</span></li>
        <li><svg class="tick" viewBox="0 0 12 12"><circle cx="6" cy="6" r="6" fill="#fff"/><path d="M3.2 6.2l1.9 1.9 3.7-3.9" stroke="#3d86c9" stroke-width="1.6" fill="none"/></svg><span>Quality Workmanship &amp; Materials</span></li>
        <li><svg class="tick" viewBox="0 0 12 12"><circle cx="6" cy="6" r="6" fill="#fff"/><path d="M3.2 6.2l1.9 1.9 3.7-3.9" stroke="#3d86c9" stroke-width="1.6" fill="none"/></svg><span><b>FREE</b> Gate Adjustments for <b>LIFE</b></span></li>
      </ul>
      <p class="fine">*some restrictions apply</p>
    </section>

    <div class="cta">
      <p class="cta-title">CALL FOR FREE ESTIMATE</p>
      <p class="cta-phone">555-014-2273</p>
      <p class="cta-links">office@mybraxtonyard.com • mybraxtonyard.com</p>
    </div>

    <h2 class="styles-title">MANY FENCE STYLES AVAILABLE</h2>
    <div class="styles">
      <div class="style-card picket" role="img" aria-label="Photo of a wood picket fence"><span class="style-label">Wood Picket</span></div>
      <div class="style-card privacy" role="img" aria-label="Photo of a wood privacy fence"><span class="style-label">Wood Privacy</span></div>
      <div class="style-card split" role="img" aria-label="Photo of an estate and split rail fence"><span class="style-label">Estate &amp; Split Rail</span></div>
      <div class="style-card aluminum" role="img" aria-label="Photo of a black aluminum fence"><span class="style-label">Aluminum</span></div>
    </div>

    <div class="footer">
      <p class="verse">Trust in the Lord with all your heart and lean not unto your own understanding in all thy ways acknowledge Him and He shall direct thy paths. <b>PROVERBS 3:5-6</b></p>
      <div class="divider"></div>
      <p class="hours"><b class="lead">READY FOR YOUR NEW FENCE?</b> <b>All estimates are free!</b><br>Estimates via phone, online, email, and in-person measurements.<br>Office hours are Monday - Thursday 9AM - 3PM and Friday 9AM - 1PM</p>
    </div>
  </div>
</body>
</html>
```